Vel CBD Pod package and logo design.

Vel is the brand name for our line of CBD Tarn style pods. I would like the logo to be designed as well as the packaging. The packaging will be the same size as the Tarn pod packaging. I would also like the box to be white and have a similar clean look just as Tarn does. My vision for the brand is very simple with black letters in a font similar to the picture attached. I would also like an animated marijuana flower that is extremely simple and also very similar to the picture attached below. Please note that I do not want the logo to be an exact copy of the example attached. I have also attached a picture of the Tarn packaging.

Although I do like my idea of the logo I am very much open to your creative ideas and will absolutely consider any other logo designs outside of my description. One final note, outside of the simple marijuana flower above the "i", I do not want the logo to scream "Marijuana" as it is a CBD product and the overt marijuana referenced brands dont fair to well to the non-marijuana user. If you have any questions, please do not hesitate to ask.

```html
<!DOCTYPE html>
<html lang="en">
<head>
<meta charset="utf-8">
<title>Vel CBD Pod Packaging</title>
<link rel="stylesheet" href="https://fonts.googleapis.com/css2?family=Nunito+Sans:wght@300;400;700&display=swap">
<style>
  :root {
    --stage: #9a9a9a;
    --stage-edge: #7d7d7d;
    --panel-mint: #e8f4f1;
    --panel-white: #ffffff;
    --panel-black: #1f1e1f;
    --ink: #2b2b2b;
    --gold: #c9a43c;
    --navy: #575a78;
    --teal: #2fb4b4;
    --green: #6abf83;
    --pod-green: #69bd7f;
    --pod-dark: #474a45;
    --numeral: #b8b8b8;
    --tag-dark: #333333;
    --tag-light: #e6e6e6;
  }
  * { margin: 0; padding: 0; box-sizing: border-box; }
  html, body { width: 1200px; height: 668px; overflow: hidden; background: var(--stage); }
  body { font-family: "Nunito Sans", sans-serif; }
  .stage {
    position: relative; width: 1200px; height: 668px;
    background: var(--stage); border: 2px solid var(--stage-edge);
  }
  .pack { position: absolute; top: 32px; width: 326px; height: 564px; }
  .pack--mint { left: 53px; background: var(--panel-mint); }
  .pack--white { left: 405px; background: var(--panel-white); }
  .pack--black { left: 793px; background: var(--panel-black); }

  .wordmark {
    position: absolute; font-weight: 300; line-height: 1;
    color: var(--ink); letter-spacing: 4px;
  }
  .pack--mint .wordmark { left: 26px; top: 40px; font-size: 96px; }
  .pack--white .wordmark { left: 0; right: 0; top: 40px; text-align: center; font-size: 100px; }
  .pack--black .wordmark { left: 0; right: 0; top: 46px; text-align: center; font-size: 96px; color: var(--gold); }

  .count {
    position: absolute; background: var(--navy); color: #fff;
    font-weight: 700; font-size: 19px; line-height: 27px; text-align: center;
  }
  .pack--mint .count { left: 0; top: 168px; width: 117px; height: 28px; }
  .pack--white .count, .pack--black .count { left: 114px; top: 234px; width: 97px; height: 25px; font-size: 18px; line-height: 25px; }

  .pods {
    position: absolute;
    background: linear-gradient(to bottom, var(--pod-green) 0%, var(--pod-green) 48%, var(--pod-dark) 52%, var(--pod-dark) 100%);
    border-radius: 4px;
  }
  .pack--mint .pods { left: 27px; top: 256px; width: 272px; height: 120px; }
  .pack--white .pods { left: 76px; top: 290px; width: 174px; height: 78px; }
  .pack--black .pods { left: 76px; top: 290px; width: 174px; height: 78px; }

  .tagline {
    position: absolute; left: 0; right: 0; text-align: center;
    font-size: 12px; color: var(--tag-dark);
  }
  .pack--mint .tagline { top: 450px; }
  .pack--white .tagline { top: 414px; }
  .pack--black .tagline { top: 414px; color: var(--tag-light); }

  .oil-label {
    position: absolute; left: 25px; top: 470px; width: 276px; height: 61px;
    background: var(--teal); color: #fff; text-align: center;
  }
  .oil-label__title { display: block; font-size: 16px; line-height: 20px; padding-top: 9px; letter-spacing: 0.5px; }
  .oil-label__doses {
    display: block; margin-top: 4px; background: var(--green);
    font-size: 14px; line-height: 20px;
  }

  .dose {
    position: absolute; left: 39px; width: 247px; height: 24px;
    color: #fff; font-size: 17px; line-height: 24px; text-align: center;
  }
  .dose--cbd { top: 440px; background: var(--teal); }
  .dose--cbg { top: 474px; background: var(--green); }
  .dose--cbc { top: 509px; background: var(--navy); }

  .numeral {
    position: absolute; top: 604px; width: 60px; text-align: center;
    font-size: 44px; font-weight: 300; color: var(--numeral); line-height: 1;
  }
</style>
</head>
<body>
<main class="stage">
  <section class="pack pack--mint">
    <div class="wordmark">Vel</div>
    <div class="count">4 Pods</div>
    <div class="pods" role="img" aria-label="Four vape pods in a row, green tops and dark bodies"></div>
    <p class="tagline">The Alternative For Adults Smokers</p>
    <div class="oil-label">
      <span class="oil-label__title">CANNABINOIDS OIL</span>
      <span class="oil-label__doses">CBD 71mg | CBG 10mg | CBC 3mg</span>
    </div>
  </section>

  <section class="pack pack--white">
    <div class="wordmark">Vel</div>
    <div class="count">4 Pods</div>
    <div class="pods" role="img" aria-label="Four vape pods in a row, green tops and dark bodies"></div>
    <p class="tagline">The Alternative For Adults Smokers</p>
    <div class="dose dose--cbd">CBD 71mg</div>
    <div class="dose dose--cbg">CBG 10mg</div>
    <div class="dose dose--cbc">CBC 3mg</div>
  </section>

  <section class="pack pack--black">
    <div class="wordmark">Vel</div>
    <div class="count">4 Pods</div>
    <div class="pods" role="img" aria-label="Four vape pods in a row, green tops and dark bodies"></div>
    <p class="tagline">The Alternative For Adults Smokers</p>
    <div class="dose dose--cbd">CBD 71mg</div>
    <div class="dose dose--cbg">CBG 10mg</div>
    <div class="dose dose--cbc">CBC 3mg</div>
  </section>

  <span class="numeral" style="left:172px">1</span>
  <span class="numeral" style="left:568px">2</span>
  <span class="numeral" style="left:966px">3</span>
</main>
</body>
</html>
```